Boutique Real Estate Brokerage looking for business card, letterhead and envelope design

We are looking for a cohesive design for our business cards, letterhead and envelopes and that mirrors our high-end homes and clientele. Fern & Gable is being launched and designed for the marketplace of tomorrow. We grew from the #1 team in our community into a full-service firm that is going to revolutionize the traditional real estate model.

We understand that it’s more important than ever to help our clients and partners adapt to behavioral and market changes being driven by generational shifts and technological advances in society, and by combining traditional brokerage services with innovative production and marketing capabilities, we know how to do that better than anyone else.

Requirements
Must have
• business card, letterhead and envelope design - attached logo.

```html
<!DOCTYPE html>
<html lang="en">
<head>
<meta charset="utf-8">
<title>Fern & Gable Realty — Stationery</title>
<link href="https://fonts.googleapis.com/css2?family=Montserrat:wght@500;700&family=Lato:ital,wght@0,400;0,700;1,400&family=Great+Vibes&display=swap" rel="stylesheet">
<style>
  :root {
    --navy: #1a0f5c;
    --gold: #c08444;
    --ink: #4a4a55;
    --muted: #8a8a92;
    --paper: #ffffff;
    --bg-top: #d6d6d6;
    --bg-mid: #efefef;
    --bg-low: #dcdcdc;
  }
  * { box-sizing: border-box; margin: 0; padding: 0; }
  html, body { width: 1200px; height: 2472px; overflow: hidden; }
  body { font-family: "Lato", sans-serif; color: var(--ink); }

  .section { position: relative; width: 1200px; }
  .section--cards { height: 820px; background: var(--bg-top); }
  .section--letterhead { height: 880px; background: var(--bg-mid); }
  .section--envelope { height: 772px; background: var(--bg-low); }

  .sheet { position: absolute; background: var(--paper); box-shadow: 0 14px 40px rgba(0,0,0,.14); overflow: hidden; }

  /* Plain edge bands: navy bar with a thin gold rule */
  .edge-band { position: absolute; left: 0; right: 0; background: var(--navy); }
  .edge-band::before { content: ""; position: absolute; left: 0; right: 0; height: 3px; background: var(--gold); }
  .edge-band--bottom { bottom: 0; }
  .edge-band--bottom::before { top: -7px; }
  .edge-band--top { top: 0; }
  .edge-band--top::before { bottom: -7px; }
  .side-rule { position: absolute; top: 0; bottom: 0; left: 0; width: 6px; background: var(--gold); }

  .wordmark { display: flex; align-items: center; gap: 10px; font-family: "Montserrat", sans-serif; font-weight: 700; color: var(--navy); text-transform: uppercase; letter-spacing: .04em; white-space: nowrap; }
  .wordmark__square { width: 1em; height: 1em; background: var(--navy); flex: none; }

  .contact-list { list-style: none; }
  .contact-list li { display: flex; align-items: center; gap: 10px; }
  .contact-list svg { flex: none; fill: var(--gold); }

  /* Business cards */
  .card { width: 500px; height: 286px; top: 267px; }
  .card--front { left: 80px; display: flex; align-items: center; justify-content: center; }
  .card--front .wordmark { font-size: 26px; }
  .card--back { left: 620px; }
  .card--back .edge-band { height: 16px; }
  .card--back .wordmark { position: absolute; left: 40px; top: 96px; font-size: 15px; }
  .card__person { position: absolute; right: 40px; top: 42px; text-align: right; font-family: "Montserrat", sans-serif; }
  .card__name { font-weight: 700; font-size: 15px; color: var(--navy); }
  .card__role { font-weight: 700; font-size: 10px; color: var(--gold); margin-top: 3px; }
  .card--back .contact-list { position: absolute; left: 40px; top: 150px; font-size: 11px; color: var(--ink); }
  .card--back .contact-list li { margin-bottom: 7px; }

  /* Letterhead */
  .letterhead { width: 580px; height: 820px; left: 310px; top: 30px; }
  .letterhead .edge-band--top { height: 14px; }
  .letterhead .edge-band--bottom { height: 22px; }
  .letterhead .wordmark { position: absolute; left: 44px; top: 70px; font-size: 16px; }
  .letter__to { position: absolute; left: 44px; top: 120px; font-size: 9px; }
  .letter__to-label { color: var(--muted); }
  .letter__to-name { font-family: "Montserrat", sans-serif; font-weight: 700; font-size: 14px; color: var(--navy); }
  .letter__to-role { color: var(--muted); margin-bottom: 8px; }
  .letter__field b { color: var(--gold); font-style: italic; font-weight: 700; }
  .letter__field { color: var(--muted); font-style: italic; line-height: 1.5; }
  .letter__date { position: absolute; right: 44px; top: 200px; font-size: 9px; font-style: italic; color: var(--muted); }
  .letter__body { position: absolute; left: 44px; right: 44px; top: 240px; font-size: 9.5px; line-height: 1.7; color: var(--muted); font-style: italic; }
  .letter__body p { margin-bottom: 12px; }
  .letter__body .lead { color: var(--ink); font-weight: 700; }
  .letter__sign { position: absolute; left: 44px; top: 440px; }
  .letter__sign-name { font-family: "Montserrat", sans-serif; font-weight: 700; font-size: 12px; color: var(--navy); }
  .letter__sign-role { font-size: 9px; color: var(--muted); }
  .letter__signature { font-family: "Great Vibes", cursive; font-size: 30px; color: #5a63c8; margin-top: 4px; }
  .letterhead .contact-list { position: absolute; left: 44px; top: 540px; font-size: 9px; color: var(--muted); }
  .letterhead .contact-list li { margin-bottom: 4px; gap: 7px; }

  /* Envelope */
  .envelope { width: 900px; height: 450px; left: 150px; top: 160px; }
  .envelope .edge-band--bottom { height: 26px; }
  .envelope .wordmark { position: absolute; left: 90px; top: 120px; font-size: 30px; }
  .envelope .contact-list { position: absolute; left: 110px; top: 220px; font-size: 19px; color: var(--ink); }
  .envelope .contact-list li { margin-bottom: 10px; gap: 14px; }
</style>
</head>
<body>

<svg width="0" height="0" style="position:absolute" aria-hidden="true">
  <defs>
    <symbol id="icon-pin" viewBox="0 0 12 12"><path d="M6 0a4 4 0 0 0-4 4c0 3 4 8 4 8s4-5 4-8a4 4 0 0 0-4-4zm0 5.5A1.5 1.5 0 1 1 6 2.5a1.5 1.5 0 0 1 0 3z"/></symbol>
    <symbol id="icon-phone" viewBox="0 0 12 12"><path d="M2.5 0.5 4.5 3 3.5 4.5c.8 1.6 2.2 3 3.8 3.8L8.8 7.3 11.3 9.3 10 11.5C5 11 1 7 .5 2z"/></symbol>
    <symbol id="icon-send" viewBox="0 0 12 12"><path d="M0 5.5 12 0 8 12 6 7z"/></symbol>
    <symbol id="icon-web" viewBox="0 0 12 12"><path d="M6 0a6 6 0 1 0 0 12A6 6 0 0 0 6 0zm0 2a4 4 0 1 1 0 8 4 4 0 0 1 0-8z"/></symbol>
  </defs>
</svg>

<section class="section section--cards" aria-label="Business card">
  <article class="sheet card card--front">
    <div class="wordmark"><span class="wordmark__square"></span>Fern &amp; Gable Realty</div>
  </article>

  <article class="sheet card card--back">
    <div class="side-rule"></div>
    <div class="edge-band edge-band--bottom"></div>
    <div class="card__person">
      <div class="card__name">YOUR FULL NAME</div>
      <div class="card__role">Designation</div>
    </div>
    <div class="wordmark"><span class="wordmark__square"></span>Fern &amp; Gable Realty</div>
    <ul class="contact-list">
      <li><svg width="10" height="10"><use href="#icon-pin"/></svg>18 Linden Row, Maple Falls, CT 06020</li>
      <li><svg width="10" height="10"><use href="#icon-phone"/></svg>(+00) 555 0142 730</li>
      <li><svg width="10" height="10"><use href="#icon-send"/></svg>info@fernandgable.com</li>
      <li><svg width="10" height="10"><use href="#icon-web"/></svg>www.fernandgable.com</li>
    </ul>
  </article>
</section>

<section class="section section--letterhead" aria-label="Letterhead">
  <article class="sheet letterhead">
    <div class="edge-band edge-band--top"></div>
    <div class="edge-band edge-band--bottom"></div>

    <div class="wordmark"><span class="wordmark__square"></span>Fern &amp; Gable Realty</div>

    <div class="letter__to">
      <div class="letter__to-label">TO</div>
      <div class="letter__to-name">Marcus</div>
      <div class="letter__to-role">Director</div>
      <div class="letter__field"><b>Address:</b> 9 Birch Lane, Oak Ridge, IL 60100</div>
      <div class="letter__field"><b>Email:</b> marcus@homeoffice.com</div>
      <div class="letter__field"><b>Phone:</b> (+00) 555 0198 240</div>
    </div>

    <div class="letter__date">Date: 27.07.2023</div>

    <div class="letter__body">
      <p>Dear Mr. Reyes,</p>
      <p>We are glad to share the details of our latest listings and the services our team offers to buyers and sellers across the region. Our advisors guide every step, from first viewing to final signing, with care and clear advice.</p>
      <p class="lead">Please review the enclosed material at your convenience and contact our office with any questions about pricing, timing or next steps.</p>
    </div>

    <div class="letter__sign">
      <div class="letter__sign-name">Your Name</div>
      <div class="letter__sign-role">Designation</div>
      <div class="letter__signature">Signature</div>
    </div>

    <ul class="contact-list">
      <li><svg width="8" height="8"><use href="#icon-pin"/></svg>18 Linden Row, Maple Falls, CT 06020</li>
      <li><svg width="8" height="8"><use href="#icon-phone"/></svg>(+00) 555 0142 730</li>
      <li><svg width="8" height="8"><use href="#icon-send"/></svg>info@fernandgable.com</li>
      <li><svg width="8" height="8"><use href="#icon-web"/></svg>www.fernandgable.com</li>
    </ul>
  </article>
</section>

<section class="section section--envelope" aria-label="Envelope">
  <article class="sheet envelope">
    <div class="side-rule"></div>
    <div class="edge-band edge-band--bottom"></div>

    <div class="wordmark"><span class="wordmark__square"></span>Fern &amp; Gable Realty</div>

    <ul class="contact-list">
      <li><svg width="14" height="14"><use href="#icon-pin"/></svg>18 Linden Row, Maple Falls, CT 06020</li>
      <li><svg width="14" height="14"><use href="#icon-phone"/></svg>(+00) 555 0142 730</li>
      <li><svg width="14" height="14"><use href="#icon-send"/></svg>info@fernandgable.com</li>
      <li><svg width="14" height="14"><use href="#icon-web"/></svg>www.fernandgable.com</li>
    </ul>
  </article>
</section>

</body>
</html>
```